Freelance Translator in Need of a Business Card

I am a freelance Japanese to English translator. I work in the video game localization industry and do literary translation in my spare time. I would like to have both the English word 'Translator' and the Japanese '翻訳者' in the job title. The final design should evoke trust, openness, and reliability.

Target Market(s)

Video game localization companies
Japanese comic book artists

Industry/Entity Type

Business

Contact Information for Business Card

Daniel Ostrowik, Translator
dan.ostrowik@quellbox.net
verolingworks.com
twitter: @verol_tx

Colors

Designer to choose colors to be used in the design.

```html
<!DOCTYPE html>
<html lang="en">
<head>
<meta charset="utf-8">
<title>Daniel Ostrowik — Translator business card</title>
<link rel="stylesheet" href="https://fonts.googleapis.com/css2?family=Ubuntu:wght@400;500;700&family=Noto+Sans+JP:wght@400&display=swap">
<style>
  :root {
    --page: #e6e7e9;
    --card-white: #ffffff;
    --card-dark: #3b3b3d;
    --blue: #1a72c4;
    --ink: #1e1e1e;
    --rule: #1b1b1b;
    --stripe: #eeeef1;
    --art-light: #ececee;
    --art-dark: #48484b;
  }
  * { box-sizing: border-box; margin: 0; padding: 0; }
  html, body { width: 1200px; height: 1200px; overflow: hidden; }
  body {
    background: var(--page);
    font-family: "Ubuntu", "Noto Sans JP", sans-serif;
    position: relative;
  }
  .card {
    position: absolute;
    left: 150px;
    width: 900px;
    height: 514px;
    border-radius: 4px;
    box-shadow: 0 6px 22px rgba(0,0,0,0.12);
    overflow: hidden;
  }
  .card--front { top: 46px; background: var(--card-white); }
  .card--back { top: 640px; background: var(--card-dark); }

  /* front */
  .name-band {
    position: absolute; left: 0; top: 46px;
    width: 430px; height: 104px;
    background: var(--blue);
    color: #fff;
    padding: 16px 0 0 60px;
  }
  .name-band__name { font-size: 40px; font-weight: 500; letter-spacing: -0.5px; }
  .name-band__title { font-size: 23px; font-weight: 400; margin-top: 6px; }
  .name-band__title .jp { font-family: "Noto Sans JP", sans-serif; }
  .name-rule {
    position: absolute; left: 0; top: 156px;
    width: 430px; height: 6px; background: var(--rule);
  }
  .contacts {
    position: absolute; left: 60px; top: 214px;
    list-style: none;
  }
  .contacts li {
    display: flex; align-items: center; gap: 14px;
    font-size: 25px; color: var(--ink);
    height: 44px;
  }
  .contacts svg { width: 22px; height: 22px; flex: none; }
  .art--front {
    position: absolute; left: 470px; top: 220px;
    width: 390px; height: 260px;
    border-radius: 28px;
    background: linear-gradient(135deg, var(--art-light), #f6f6f7);
  }

  /* back */
  .art--back {
    position: absolute; left: 240px; top: 70px;
    width: 420px; height: 260px;
    border-radius: 28px;
    background: linear-gradient(135deg, var(--art-dark), #414144);
  }
  .url-stripe {
    position: absolute; left: 0; top: 392px;
    width: 100%; height: 64px;
    background: var(--stripe);
    display: flex; align-items: center;
    padding-left: 60px;
  }
  .url-stripe__text { color: var(--blue); font-size: 28px; font-weight: 500; }
</style>
</head>
<body>

<section class="card card--front" aria-label="Card front">
  <div class="name-band">
    <div class="name-band__name">Daniel Ostrowik</div>
    <div class="name-band__title">Translator, <span class="jp">翻訳者</span></div>
  </div>
  <div class="name-rule"></div>

  <ul class="contacts">
    <li>
      <svg viewBox="0 0 22 22" aria-hidden="true"><circle cx="11" cy="11" r="10" fill="var(--blue)"/><path d="M7 6.5c.6-.6 1.4-.6 1.8 0l1 1.5c.3.5.2 1-.2 1.4l-.6.6c.6 1.3 1.6 2.3 2.9 2.9l.6-.6c.4-.4.9-.5 1.4-.2l1.5 1c.6.4.6 1.2 0 1.8-1.4 1.4-3.6.9-5.8-1.3S5.6 7.9 7 6.5z" fill="#fff"/></svg>
      555 014 2208
    </li>
    <li>
      <svg viewBox="0 0 22 22" aria-hidden="true"><circle cx="11" cy="11" r="10" fill="var(--blue)"/><rect x="5.5" y="7" width="11" height="8" rx="1" fill="#fff"/><path d="M5.8 7.4 11 11.4l5.2-4" fill="none" stroke="var(--blue)" stroke-width="1.2"/></svg>
      dan.ostrowik@quellbox.net
    </li>
    <li>
      <svg viewBox="0 0 22 22" aria-hidden="true"><circle cx="11" cy="11" r="10" fill="var(--blue)"/><circle cx="11" cy="11" r="6" fill="none" stroke="#fff" stroke-width="1.3"/><ellipse cx="11" cy="11" rx="2.6" ry="6" fill="none" stroke="#fff" stroke-width="1.2"/><path d="M5 11h12" stroke="#fff" stroke-width="1.2"/></svg>
      www.verolingworks.com
    </li>
    <li>
      <svg viewBox="0 0 22 22" aria-hidden="true"><circle cx="11" cy="11" r="10" fill="var(--blue)"/></svg>
      @verol_tx
    </li>
  </ul>

  <div class="art art--front" role="img" aria-label="Hand-drawn pair of speech bubbles, one holding the Japanese kana あ and one the letter A"></div>
</section>

<section class="card card--back" aria-label="Card back">
  <div class="art art--back" role="img" aria-label="Hand-drawn pair of speech bubbles in white outline, one holding the Japanese kana あ and one the letter A"></div>
  <div class="url-stripe">
    <span class="url-stripe__text">www.verolingworks.com</span>
  </div>
</section>

</body>
</html>
```